Pounce! A stand up comedy show- poster and other graphics required

We require a design for a new late night comedy show called 'Pounce!' which will appear at festivals and feature a variety of stand up acts as well as inviting the audience to heckle the comedians on stage. The final design should be bold and stand out loudly, to fit the late night raucous nature of the show.
We need a poster image as well as smaller images for program guides and websites. This is going to be the kind of show people talk about so needs a poster to match!!

Target Market(s)

Comedy fans, 20-40 year olds, late night adult audience

Requirements
Nice to have
• We don't really have any clear design in mind so happy to leave it to interpretation but possible ideas would be: a silhouette of a head shouting / a mic is always an iconic image / the simple outline of an audience with obscenities (@*!& etc) coming out of them / perhaps a mic having fallen over because of a stand-up running off stage!
• But again these are vague ideas. Please message for more info about the show if it helps
Should not have
• Not too busy

```html
<!DOCTYPE html>
<html lang="en">
<head>
<meta charset="utf-8">
<title>Pounce! – Late Night Stand Up</title>
<link rel="stylesheet" href="https://fonts.googleapis.com/css2?family=Playfair+Display:wght@400&family=Arimo:wght@400;700&display=swap">
<style>
  :root {
    --backdrop: #98999b;
    --poster-black: #0b0708;
    --spot-red: #e8321a;
    --spot-deep: #8a1408;
    --title-red: #ee3418;
    --text-white: #ffffff;
  }
  html, body {
    margin: 0;
    padding: 0;
    width: 914px;
    height: 1200px;
    overflow: hidden;
    background: var(--backdrop);
  }
  .poster {
    position: absolute;
    left: 123px;
    top: 127px;
    width: 668px;
    height: 945px;
    background: var(--poster-black);
    overflow: hidden;
  }
  .spotlight {
    position: absolute;
    left: 86px;
    top: 48px;
    width: 540px;
    height: 475px;
    border-radius: 50%;
    background: radial-gradient(ellipse at 50% 45%, var(--spot-red) 0%, #d42a12 55%, var(--spot-deep) 85%, rgba(11,7,8,0) 100%);
  }
  .title {
    position: absolute;
    left: 0;
    top: 560px;
    width: 668px;
    height: 220px;
  }
  .title text {
    font-family: "Playfair Display", "Bodoni Moda", serif;
    font-weight: 400;
    fill: var(--title-red);
  }
  .tagline {
    position: absolute;
    left: 0;
    width: 668px;
    text-align: center;
    font-family: "Arimo", Arial, sans-serif;
    margin: 0;
  }
  .tagline--acts {
    top: 773px;
    left: 5px;
    font-size: 17px;
    font-weight: 700;
    color: var(--title-red);
  }
  .tagline--invite {
    top: 822px;
    left: 2px;
    font-size: 17px;
    line-height: 22px;
    font-weight: 400;
    color: var(--text-white);
  }
</style>
</head>
<body>
  <main class="poster">
    <div class="spotlight" role="img" aria-label="Photograph of a vintage microphone on a stand before a red stage curtain, lit by a round spotlight"></div>
    <svg class="title" viewBox="0 0 668 220" aria-label="Pounce!">
      <text x="109" y="205" font-size="250" textLength="476" lengthAdjust="spacingAndGlyphs">POUNCE!</text>
    </svg>
    <p class="tagline tagline--acts">A VARIETY OF STAND UP ACTS</p>
    <p class="tagline tagline--invite">INVITING THE AUDIENCE TO HECKLE<br>THE COMEDIANS ON STAGE</p>
  </main>
</body>
</html>
```